Infographic for Anesthesia Management Company

I would like my Anesthesia Management company, Veltrin Anesthesia, service information placed into a infographic for use on a brochure and webpage. Please focus on just the infographic.
-Veltrin Services text to be placed into infographic attached in word file.
-Two Vector infographic templates attached as well. I am open to either option, or alternative layout suggestion.
-Please match color scheme to veltrinanesthesia-example.com
-Veltrin logo attached.
Thank you for your help!
Marvin
Target Market(s)
Surgery Centers
Industry/Entity Type
It Company
Font styles to use
Requirements
Must have
- Professional Look.
- Easy to read text.
- Cohesive branding
Nice to have
- Please see attached Vector examples.

```html
<!DOCTYPE html>
<html lang="en">
<head>
<meta charset="utf-8">
<title>Veltrin Anesthesia – Service Infographic</title>
<link rel="stylesheet" href="https://fonts.googleapis.com/css2?family=Poppins:wght@300;400;500;600;700&display=swap">
<style>
  :root {
    --canvas: #ffffff;
    --ink: #2b2b2b;
    --ink-soft: #555555;
    --red: #e0262b;
    --red-deep: #a8161b;
    --grey-light: #c4c4c4;
    --grey-light-deep: #8f8f8f;
    --grey-dark: #6a6a6a;
    --grey-dark-deep: #3a3a3a;
    --teal: #1ba88c;
    --teal-deep: #0b7462;
    --band: #ececec;
  }
  html, body {
    margin: 0;
    width: 1200px;
    height: 1162px;
    overflow: hidden;
    background: var(--canvas);
    font-family: "Poppins", sans-serif;
  }
  .infographic {
    position: absolute;
    left: 22px;
    top: 219px;
    width: 1156px;
    height: 724px;
  }
  .item-title { font-size: 8px; font-weight: 500; fill: var(--ink); }
  .item-body { font-size: 5.2px; font-weight: 300; fill: var(--ink-soft); }
  .tier-letter { font-size: 38px; font-weight: 700; fill: #ffffff; text-anchor: middle; }
  .tier-label { font-size: 7.4px; font-weight: 400; fill: #ffffff; }
  .icon-ring { fill: none; stroke: #ffffff; stroke-width: 1.6; }
  .icon-line { fill: none; stroke: #ffffff; stroke-width: 2.2; stroke-linecap: round; stroke-linejoin: round; }
  .brand-name { font-size: 22px; font-weight: 600; fill: var(--teal); text-anchor: middle; }
  .tagline { font-size: 15px; font-weight: 300; fill: var(--teal); text-anchor: middle; }
</style>
</head>
<body>
<svg class="infographic" viewBox="0 0 680 426" xmlns="http://www.w3.org/2000/svg">
  <defs>
    <linearGradient id="band" x1="0" y1="0" x2="0" y2="1">
      <stop offset="0" stop-color="#ffffff"/>
      <stop offset="0.75" stop-color="#f6f6f6"/>
      <stop offset="1" stop-color="var(--band)"/>
    </linearGradient>
    <linearGradient id="fade" x1="0" y1="0" x2="1" y2="0">
      <stop offset="0" stop-color="#fff" stop-opacity="1"/>
      <stop offset="0.08" stop-color="#fff" stop-opacity="0"/>
      <stop offset="0.92" stop-color="#fff" stop-opacity="0"/>
      <stop offset="1" stop-color="#fff" stop-opacity="1"/>
    </linearGradient>
    <linearGradient id="tier-red" x1="0" y1="0" x2="1" y2="1">
      <stop offset="0" stop-color="var(--red)"/>
      <stop offset="1" stop-color="var(--red-deep)"/>
    </linearGradient>
    <linearGradient id="tier-grey" x1="0" y1="0" x2="1" y2="1">
      <stop offset="0" stop-color="var(--grey-light)"/>
      <stop offset="1" stop-color="var(--grey-light-deep)"/>
    </linearGradient>
    <linearGradient id="tier-dark" x1="0" y1="0" x2="1" y2="1">
      <stop offset="0" stop-color="var(--grey-dark)"/>
      <stop offset="1" stop-color="var(--grey-dark-deep)"/>
    </linearGradient>
    <linearGradient id="tier-teal" x1="0" y1="0" x2="1" y2="1">
      <stop offset="0" stop-color="var(--teal)"/>
      <stop offset="1" stop-color="var(--teal-deep)"/>
    </linearGradient>
    <linearGradient id="rule" x1="0" y1="0" x2="1" y2="0">
      <stop offset="0" stop-color="var(--red)"/>
      <stop offset="0.16" stop-color="var(--red)"/>
      <stop offset="0.2" stop-color="#3a2a2a"/>
      <stop offset="0.3" stop-color="#3a2a2a"/>
      <stop offset="0.33" stop-color="var(--teal)"/>
      <stop offset="0.52" stop-color="var(--teal)"/>
      <stop offset="0.56" stop-color="#1e3b36"/>
      <stop offset="0.75" stop-color="#2a2a2a"/>
      <stop offset="1" stop-color="#2a2a2a"/>
    </linearGradient>
  </defs>

  <!-- background bands -->
  <g class="bands">
    <rect x="20" y="18" width="640" height="76" fill="url(#band)"/>
    <rect x="20" y="94" width="640" height="68" fill="url(#band)"/>
    <rect x="20" y="162" width="640" height="72" fill="url(#band)"/>
    <rect x="20" y="234" width="640" height="71" fill="url(#band)"/>
    <rect x="20" y="18" width="640" height="287" fill="url(#fade)"/>
  </g>

  <!-- tiers -->
  <g class="tier tier-a">
    <polygon points="291,234 381,234 337,378 247,378" fill="url(#tier-teal)"/>
    <text class="tier-letter" x="322" y="284">A</text>
    <text class="tier-label" x="282" y="299">PROFESSIONALISM</text>
    <circle class="icon-ring" cx="302" cy="338" r="20"/>
    <path class="icon-line" d="M288 337 l6 -6 h5 l4 3 l4 -3 h3 l5 6 M294 340 l5 5 M298 337 l6 6 M302 335 l6 6 M306 334 l5 5"/>
  </g>
  <g class="tier tier-b">
    <polygon points="235,162 325,162 280,305 190,305" fill="url(#tier-dark)"/>
    <text class="tier-letter" x="266" y="212">B</text>
    <text class="tier-label" x="226" y="227">ACCOUNTABILITY</text>
    <circle class="icon-ring" cx="248" cy="264" r="20"/>
    <rect class="icon-line" x="239" y="255" width="17" height="17" rx="1.5"/>
    <path class="icon-line" d="M242 262 l5 5 l11 -13"/>
  </g>
  <g class="tier tier-c">
    <polygon points="177,90 267,90 222,234 132,234" fill="url(#tier-grey)"/>
    <text class="tier-letter" x="208" y="139">C</text>
    <text class="tier-label" x="183" y="152">EFFICIENCY</text>
    <circle class="icon-ring" cx="182" cy="198" r="20"/>
    <circle class="icon-line" cx="182" cy="200" r="9"/>
    <path class="icon-line" d="M182 188 v2 M179 188 h6 M182 200 l4 -4"/>
  </g>
  <g class="tier tier-d">
    <polygon points="121,18 210,18 164,162 75,162" fill="url(#tier-red)"/>
    <text class="tier-letter" x="155" y="67">D</text>
    <text class="tier-label" x="113" y="89">PATIENT SAFETY</text>
    <circle class="icon-ring" cx="127" cy="126" r="20"/>
    <rect x="119" y="124" width="16" height="12" rx="1.5" fill="#ffffff"/>
    <path class="icon-line" d="M122 124 v-4 a5 5 0 0 1 10 0 v4"/>
    <circle cx="127" cy="129" r="1.6" fill="var(--red)"/>
  </g>

  <!-- copy -->
  <g class="copy copy-d">
    <text class="item-title" x="226" y="31">Clinical Guidance and Quality Improvement</text>
    <text class="item-body" x="226" y="42">•  Veltrin implements clinical guidelines to ensure patient safety and satisfaction, including:</text>
    <text class="item-body" x="226" y="51">1.  Pre-operative guideline protocols to minimize cancellations and optimize patient outcomes</text>
    <text class="item-body" x="226" y="61">2.  Patient selection criteria to ensure suitable surgical candidates</text>
    <text class="item-body" x="226" y="70">3.  Education programs to engage the clinical staff</text>
    <text class="item-body" x="226" y="80">4.  Evidence based multimodal pain management protocol to facilitate a timely discharge and reduce patient side effects</text>
  </g>
  <g class="copy copy-c">
    <text class="item-title" x="288" y="108">Thought Leadership</text>
    <text class="item-body" x="288" y="119">Stipend free anesthesia services</text>
    <text class="item-body" x="288" y="129">•  Proprietary and data-driven process to improve surgery flow</text>
    <text class="item-body" x="288" y="139">•  Veltrin's clinical processes empower its anesthesia providers to help the surgery center team excel</text>
    <text class="item-body" x="288" y="148">in the perioperative setting</text>
  </g>
  <g class="copy copy-b">
    <text class="item-title" x="345" y="176">In-House Billing</text>
    <text class="item-body" x="345" y="186">•  Veltrin streamlines the billing process</text>
    <text class="item-body" x="345" y="196">•  We have dedicated staff that ensures all records are processed correctly the first time</text>
    <text class="item-title" x="345" y="205">Meeting Accreditation Requirements</text>
    <text class="item-body" x="345" y="215">•  Veltrin partners with your surgery center to ensure all things pertaining to anesthesia are</text>
    <text class="item-body" x="345" y="224">up to current ASC credentialing standards</text>
  </g>
  <g class="copy copy-a">
    <text class="item-title" x="401" y="248">ASC Stakeholder Satisfaction</text>
    <text class="item-body" x="401" y="259">•  Veltrin shares its personal network of highly qualified anesthesia providers</text>
    <text class="item-body" x="401" y="269">•  We strive to create continuity between anesthesia, surgeon, and ASC staff</text>
    <text class="item-body" x="401" y="280">•  Provide ample staffing according to your scheduled case volume</text>
    <text class="item-body" x="401" y="290">•  Veltrin guarantees every anesthesia provider upholds clinical excellence</text>
  </g>

  <!-- brand -->
  <text class="brand-name" x="501" y="350">Veltrin Anesthesia</text>

  <!-- footer -->
  <rect x="36" y="383" width="611" height="2.2" fill="url(#rule)"/>
  <text class="tagline" x="343" y="407">ANESTHESIA PROVIDER RECRUITMENT, CREDENTIALING, AND STAFFING</text>
</svg>
</body>
</html>
```